MORVEN EHS & S Resources

We would like ArtHively to update and make our environmental, health and safety resources business website more professional and using our new logo and color scheme.
https://morvenehsresources.example/

```html
<!DOCTYPE html>
<html lang="en">
<head>
<meta charset="utf-8">
<title>MORVEN EHS &amp; S Resources</title>
<link href="https://fonts.googleapis.com/css2?family=Ubuntu:wght@400;500;700&family=Lato:wght@400;700&family=Roboto+Condensed:wght@400;500&display=swap" rel="stylesheet">
<style>
:root{
  --red:#e8232a;
  --blue:#1f9fdc;
  --cyan:#1aa3dd;
  --lime:#cbd821;
  --ink:#1c1c1c;
  --grey:#555;
  --dark:#1a1b1d;
  --white:#fff;
}
*{margin:0;padding:0;box-sizing:border-box}
html,body{width:1200px;height:4126px;overflow:hidden}
body{position:relative;background:var(--white);font-family:"Lato",sans-serif;color:var(--ink)}
.abs{position:absolute}
.head{font-family:"Ubuntu",sans-serif}

/* top bar */
.topbar{left:0;top:0;width:1200px;height:39px;background:var(--red);color:#fff;font:500 13px "Ubuntu",sans-serif}
.topbar span{position:absolute;top:11px}
.topbar .sep{position:absolute;top:0;width:3px;height:39px;background:#fff;transform:skewX(-22deg)}
.social{display:flex;gap:6px;position:absolute}
.social i{display:block;width:20px;height:20px;border-radius:50%;background:#fff}

/* nav */
.nav{left:0;top:39px;width:1200px;height:79px;background:#fff;border-bottom:1px solid #eee}
.brand{position:absolute;font:700 36px "Ubuntu",sans-serif;color:var(--ink);letter-spacing:1px;display:flex;align-items:center;gap:10px}
.brand b{display:block;width:22px;height:22px;background:var(--red)}
.menu{position:absolute;left:435px;top:34px;display:flex;gap:36px;font:400 14px "Ubuntu",sans-serif;color:#333}
.menu .on{color:var(--red)}
.btn-contact{position:absolute;left:919px;top:22px;width:130px;height:46px;background:var(--lime);font:500 15px "Ubuntu",sans-serif;line-height:46px;padding-left:18px;color:var(--ink)}

/* hero */
.hero{left:0;top:118px;width:1200px;height:660px}
.hero-text{left:112px;color:#fff}
.btn{position:absolute;height:48px;font:700 14px "Ubuntu",sans-serif;line-height:48px;padding-left:20px}
.btn-blue{background:var(--blue);color:#fff}
.btn-white{background:#fff;color:var(--ink)}

/* sections */
.title{width:1200px;text-align:center;font:500 44px "Ubuntu",sans-serif;color:var(--ink)}
.sub{width:1200px;text-align:center;font:500 27px "Ubuntu",sans-serif;color:var(--cyan)}
.card{position:absolute;top:948px;width:319px;height:350px;overflow:hidden}
.card .ph{position:absolute;inset:0}
.card .num{position:absolute;right:10px;bottom:-18px;font:700 70px "Ubuntu",sans-serif;color:rgba(0,0,0,.07)}
.card-label{position:absolute;top:1279px;font:500 17px "Ubuntu",sans-serif;color:var(--ink)}

.band{left:0;width:1200px}
.para{font-size:13px;line-height:29px;color:#fff;text-align:justify}
.sec-p{width:1200px;text-align:center;font-size:13px;line-height:26px;color:#333}
.tri-label{position:absolute;top:2538px;width:240px;text-align:center;font:500 16px "Roboto Condensed",sans-serif;color:var(--ink)}

/* contact */
.form-card{left:445px;top:3271px;width:606px;height:414px;background:#fff;box-shadow:0 6px 30px rgba(0,0,0,.15)}
.field{position:absolute;width:240px;border-bottom:1px solid #bbb;padding-bottom:8px}
.field label{display:block;font:400 15px "Roboto Condensed",sans-serif;color:#222;margin-bottom:12px}
.field span{font:400 13px "Roboto Condensed",sans-serif;color:#888}

/* footer */
.footer{left:0;top:3770px;width:1200px;height:312px;background:var(--dark);color:#fff}
.fcol h4{font:500 18px "Ubuntu",sans-serif;margin-bottom:8px}
.fcol .rule{width:40px;height:2px;background:var(--lime);margin-bottom:16px}
.fcol li{list-style:none;font-size:12px;line-height:27px}
.fcol li::before{content:"› ";}
.info{font-size:12px;line-height:18px}
.copy{left:0;top:4082px;width:1200px;height:44px;background:var(--red);color:#fff;font-size:11px;line-height:44px;padding-left:112px}
</style>
</head>
<body>

<!-- Top bar -->
<div class="abs topbar">
  <svg class="abs" style="left:112px;top:12px" width="12" height="16" viewBox="0 0 12 16"><path d="M6 0a6 6 0 0 1 6 6c0 4-6 10-6 10S0 10 0 6a6 6 0 0 1 6-6z" fill="#fff"/><circle cx="6" cy="6" r="2.3" fill="#e8232a"/></svg>
  <span style="left:142px">Lorem Ipsum,Usa -437916</span>
  <div class="sep" style="left:335px"></div>
  <svg class="abs" style="left:356px;top:12px" width="15" height="15" viewBox="0 0 24 24"><path d="M6.6 10.8a15 15 0 0 0 6.6 6.6l2.2-2.2a1 1 0 0 1 1-.2c1.1.4 2.3.6 3.6.6a1 1 0 0 1 1 1V20a1 1 0 0 1-1 1A17 17 0 0 1 3 4a1 1 0 0 1 1-1h3.5a1 1 0 0 1 1 1c0 1.3.2 2.5.6 3.6a1 1 0 0 1-.2 1z" fill="#fff"/></svg>
  <span style="left:381px">(555) 014 - 2290</span>
  <div class="sep" style="left:520px"></div>
  <svg class="abs" style="left:543px;top:13px" width="16" height="12" viewBox="0 0 16 12"><rect width="16" height="12" fill="#fff"/><path d="M0 0l8 6 8-6" stroke="#e8232a" stroke-width="1.5" fill="none"/></svg>
  <span style="left:570px">info@morvenehs.example</span>
  <div class="sep" style="left:785px"></div>
  <span style="left:906px">Follow Us:</span>
  <div class="social" style="left:975px;top:10px" aria-label="Social links"><i></i><i></i><i></i><i></i></div>
</div>

<!-- Navigation -->
<div class="abs nav">
  <div class="brand" style="left:112px;top:18px"><b></b>MORVEN</div>
  <nav class="menu"><span class="on">Home</span><span>About Us</span><span>Our Services</span><span>Security</span></nav>
  <svg class="abs" style="left:449px;top:69px" width="12" height="10"><path d="M6 0l6 10H0z" fill="#e8232a"/></svg>
  <div class="btn-contact">Contact Us</div>
</div>

<!-- Hero -->
<svg class="abs hero" viewBox="0 0 1200 660" width="1200" height="660">
  <defs>
    <linearGradient id="heroG" x1="0" y1="0" x2="1" y2="0">
      <stop offset="0" stop-color="#1a1614"/><stop offset=".55" stop-color="#5a4129"/><stop offset="1" stop-color="#3a2d24"/>
    </linearGradient>
  </defs>
  <rect width="1200" height="660" fill="url(#heroG)" role="img" aria-label="Two safety engineers in hard hats reviewing plans on a site"/>
  <polygon points="0,450 600,642 0,514" fill="var(--red)"/>
  <polygon points="0,514 600,642 0,660" fill="#fff"/>
  <polygon points="600,642 1200,352 1200,660" fill="#fff"/>
  <polygon points="600,642 1200,340 1200,352" fill="var(--red)"/>
  <rect x="0" y="642" width="1200" height="18" fill="#fff"/>
</svg>
<div class="abs hero-text head" style="top:246px;font-size:21px;font-weight:500">Welcome To</div>
<div class="abs hero-text head" style="top:288px;font-size:88px;font-weight:700;line-height:1">MORVEN</div>
<div class="abs hero-text head" style="top:398px;font-size:30px;font-weight:500">EHS&amp;S RESOURCES</div>
<div class="btn btn-blue" style="left:110px;top:453px;width:170px">Get Started</div>

<!-- Services -->
<div class="abs title" style="top:800px">Our Services</div>
<div class="abs sub" style="top:870px">Environmental health and safety services</div>

<div class="card" style="left:85px">
  <div class="ph" style="background:linear-gradient(135deg,#3d3a37,#8c8a86)" role="img" aria-label="Consultants in a meeting around a table"></div>
  <svg class="abs" style="left:0;top:0" width="319" height="350"><polygon points="240,150 319,300 319,350 150,350" fill="#fff"/><polygon points="264,238 310,320 218,320" fill="var(--red)"/><path d="M252 300h24v-10h-24zM258 290v-8h12v8" stroke="#fff" stroke-width="2" fill="none"/></svg>
  <div class="num">01</div>
</div>
<div class="card-label" style="left:283px">EHS Consulting</div>

<div class="card" style="left:441px">
  <div class="ph" style="background:linear-gradient(135deg,#2f3a36,#a4a89a)" role="img" aria-label="Workers in protective suits inside an industrial plant"></div>
  <svg class="abs" style="left:0;top:0" width="319" height="350"><polygon points="240,150 319,300 319,350 150,350" fill="#fff"/><polygon points="264,238 310,320 218,320" fill="var(--red)"/><path d="M252 302v-14l8 6v-6l8 6v-12h6v20z" stroke="#fff" stroke-width="2" fill="none"/></svg>
  <div class="num">02</div>
</div>
<div class="card-label" style="left:632px">Industrial Hygiene</div>

<div class="card" style="left:796px">
  <div class="ph" style="background:linear-gradient(135deg,#3b4a66,#c9b49a)" role="img" aria-label="Worker affected by chemical fumes helped by a colleague"></div>
  <svg class="abs" style="left:0;top:0" width="319" height="350"><polygon points="240,150 319,300 319,350 150,350" fill="#fff"/><polygon points="264,238 310,320 218,320" fill="var(--red)"/><circle cx="264" cy="294" r="9" stroke="#fff" stroke-width="2" fill="none"/><path d="M260 294h8M264 290v8" stroke="#fff" stroke-width="2"/></svg>
  <div class="num">03</div>
</div>
<div class="card-label" style="left:979px">Occupational Health</div>

<div class="btn btn-blue" style="left:567px;top:1336px;width:131px">View All</div>

<!-- About -->
<svg class="abs band" style="top:1471px" width="1200" height="540" viewBox="0 0 1200 540">
  <rect width="1200" height="540" fill="#6b6f74" role="img" aria-label="Engineer in hard hat reviewing a tablet at an office desk"/>
  <polygon points="0,0 835,0 528,540 0,540" fill="var(--blue)"/>
  <polygon points="838,0 858,0 1200,520 1200,540 1172,540" fill="#fff"/>
</svg>
<div class="abs head" style="left:112px;top:1530px;font-size:44px;font-weight:700;color:#fff">About US</div>
<div class="abs head" style="left:114px;top:1598px;font-size:20px;font-weight:500;color:#fff">We have Education, Experience &amp; Credentials you can Trust!</div>
<p class="abs para" style="left:110px;top:1652px;width:490px">Our Principal, Dana Reyes, PE, CSP, STS, FASSP has over 45 years of experience in the Environmental, Health, Safety and Security Management field. This experience includes industry segments such as Construction in Civil Power, Automotive, Commercial, Industrial, Semiconductor and Oil &amp; Gas, Healthcare, Manufacturing, Department of Defense and Department of Energy. He has held senior level leadership positions in professional associations (SPA, CSB, NSC) and serves on the Ashford State University OSH Advisory Board.</p>
<div class="btn btn-white" style="left:110px;top:1874px;width:146px;height:45px;line-height:45px">Read More</div>

<!-- Security -->
<div class="abs title" style="top:2092px">Our Security</div>
<div class="abs sub" style="top:2158px;font-size:21px">We are Committed to Delivering Top Quality Security to our Clients.</div>
<p class="abs sec-p" style="top:2202px">MORVEN security is a full-service security company with capabilities both nationally and internationally MORVEN provides armed<br>and unarmed executive protection details and guard services security for meetings and events protection and transportation<br>escort details for high value assets and a wide range of corporate and private investigative services.</p>
<p class="abs sec-p" style="top:2288px">MORVEN offers comprehensive physical security site assessments a suite of workforce training programs and numerous consulting and<br>technical services that can be provided on an as needed basis to provide security and inform executive level decision making.</p>

<svg class="abs" style="left:0;top:2380px" width="1200" height="150">
  <g fill="none" stroke-width="7">
    <polygon points="219,12 290,138 148,138" stroke="var(--blue)"/>
    <polygon points="473,12 544,138 402,138" stroke="var(--lime)"/>
    <polygon points="726,12 797,138 655,138" stroke="var(--blue)"/>
    <polygon points="980,12 1051,138 909,138" stroke="var(--lime)"/>
  </g>
  <g fill="none" stroke="#222" stroke-width="2">
    <path d="M219 80l14 5v10c0 9-7 14-14 17-7-3-14-8-14-17V85z"/><path d="M212 96l5 5 9-10"/>
    <ellipse cx="473" cy="98" rx="18" ry="7"/><ellipse cx="473" cy="98" rx="18" ry="7" transform="rotate(60 473 98)"/><ellipse cx="473" cy="98" rx="18" ry="7" transform="rotate(-60 473 98)"/>
    <rect x="708" y="84" width="36" height="26"/><path d="M714 104l8-8 6 5 10-12"/>
    <path d="M962 114V96h36v18M968 96v-8h24v8M975 114v-8h10v8"/>
  </g>
  <g fill="#e9eef3">
    <path d="M312 62h50v-14l24 26-24 26V86h-50z"/><path d="M566 62h50v-14l24 26-24 26V86h-50z"/><path d="M820 62h50v-14l24 26-24 26V86h-50z"/>
  </g>
</svg>
<div class="tri-label" style="left:94px">Executive Protection Services</div>
<div class="tri-label" style="left:348px">Physical Security Site Assessment</div>
<div class="tri-label" style="left:604px">Workforce Training Services</div>
<div class="tri-label" style="left:858px">School Safety and Security Services</div>

<!-- Why choose -->
<svg class="abs band" style="top:2648px" width="1200" height="484" viewBox="0 0 1200 484">
  <rect width="1200" height="484" fill="#8a8378" role="img" aria-label="Two engineers in hard hats studying blueprints beside a laptop"/>
  <polygon points="0,0 782,0 553,484 0,484" fill="var(--blue)"/>
  <polygon points="784,0 796,0 567,484 555,484" fill="#fff"/>
</svg>
<div class="abs head" style="left:114px;top:2702px;font-size:44px;font-weight:700;color:#fff">Why Choose Us</div>
<p class="abs head" style="left:110px;top:2788px;width:600px;font-size:17px;line-height:28px;color:#fff">MORVEN EHS &amp; Security resources is a woman-owned business providing EHS program development, training, consulting and skilled professional staffing.</p>
<p class="abs" style="left:110px;top:2852px;width:540px;font-size:12px;line-height:22px;color:#fff">MORVEN was established to provide clients in all industries with safety, health, environmental, and security resources that have the experience necessary to meet unique client requirements. We utilize our extensive network of professional contacts and robust vetting process to bring forward top talent to carry out our client's objectives.</p>
<p class="abs" style="left:110px;top:2950px;width:500px;font-size:12px;line-height:22px;color:#fff">Organizations understand the presence of EHS and Security personnel representing owner's businesses or contract firms are critical to maintain incident and injury free projects while assuring efficient operations.</p>
<div class="btn btn-white" style="left:110px;top:3036px;width:146px;height:43px;line-height:43px">Read More</div>

<!-- Contact -->
<div class="abs" style="left:127px;top:3225px;width:383px;height:389px;background:linear-gradient(135deg,#5c4a3a,#c08a4a)" role="img" aria-label="Engineers in hard hats pointing at a construction site"></div>
<div class="abs" style="left:750px;top:3255px;width:325px;height:309px;border:2px solid var(--red)"></div>
<div class="abs form-card">
  <div class="abs head" style="left:51px;top:34px;font-size:42px;font-weight:500">Get&nbsp; In Touch</div>
  <div class="field" style="left:51px;top:100px"><label>YOUR NAME</label><span>Jhon Smith</span></div>
  <div class="field" style="left:318px;top:100px"><label>LAST NAME</label><span>Ken</span></div>
  <div class="field" style="left:51px;top:186px"><label>EMAIL*</label><span>info@morven.example</span></div>
  <div class="field" style="left:318px;top:186px"><label>PHONE</label><span>555 014 - 2290</span></div>
  <div class="field" style="left:51px;top:276px;width:470px"><label>MESSAGE</label><span>Hi , Do you have Mpment To Talk About Us</span><br><br></div>
  <svg class="abs" style="left:515px;top:298px" width="50" height="50"><circle cx="25" cy="25" r="25" fill="var(--blue)"/><path d="M15 25l20-9-7 20-3-8z" fill="#fff"/></svg>
</div>

<!-- Footer -->
<div class="abs footer">
  <div class="abs" style="left:0;top:0;width:1200px;height:312px;background:linear-gradient(90deg,#1a1b1d,#2a2c2e 60%,#1a1b1d)" role="img" aria-label="Faded industrial workers background"></div>
  <div class="brand" style="left:122px;top:120px;color:#fff;font-size:40px"><b></b>MORVEN</div>
  <div class="social" style="left:146px;top:220px"><i></i><i></i><i></i><i></i></div>
  <div class="abs fcol" style="left:448px;top:78px"><h4>Quick Links</h4><div class="rule"></div><ul><li>Home</li><li>About Us</li><li>Services</li><li>Security</li><li>Contact Us</li></ul></div>
  <div class="abs fcol" style="left:659px;top:78px"><h4>Other Links</h4><div class="rule"></div><ul><li>Privacy Policy</li><li>Terms &amp; Conditions</li><li>Disclaimer</li></ul></div>
  <div class="abs fcol" style="left:897px;top:78px"><h4>Contact Info</h4><div class="rule"></div>
    <div class="info">Address Location</div>
    <div class="info" style="margin:8px 0 10px 36px">Lorem Ipsum,Usa - 437916</div>
    <div class="info">Phone Number</div>
    <div class="info" style="margin:8px 0 10px 36px">555 014 - 2290</div>
    <div class="info">Email Address</div>
    <div class="info" style="margin:8px 0 0 36px">info@morven.example</div>
  </div>
  <svg class="abs" style="left:900px;top:153px" width="22" height="140">
    <circle cx="11" cy="11" r="10" fill="#fff"/><circle cx="11" cy="72" r="10" fill="#fff"/><circle cx="11" cy="133" r="10" fill="#fff"/>
    <path d="M11 5a4 4 0 0 1 4 4c0 3-4 7-4 7s-4-4-4-7a4 4 0 0 1 4-4z" fill="#1a1b1d"/>
    <path d="M7 67l3 0 1 3-2 1a7 7 0 0 0 3 3l1-2 3 1v3c-6 0-9-3-9-9z" fill="#1a1b1d"/>
    <rect x="5" y="129" width="12" height="8" fill="#1a1b1d"/>
  </svg>
</div>
<div class="abs copy">© Copyright 2024 Morven Ehs&amp;s Resources. All rights reserved.<span style="position:absolute;right:60px">C67</span></div>

</body>
</html>
```